" Temos como propósito desenvolver pessoas e proporcionar saúde transformando vidas e sorrisos. Acreditamos que a educação muda pessoas e essas transformam o mundo. E que a manutenção da saúde bucal é fundamental para a saúde geral e o aumento da auto-estima do indivíduo. Nosso principal serviço são os cursos de ortodontia para dentistas já formados (pós-graduação e cursos livres de ortodontia). Temos alguns outros cursos também para dentistas em outras áreas. "

```html
<!DOCTYPE html>
<html lang="pt-BR">
<head>
<meta charset="utf-8">
<title>Arcada – Envelope Carta</title>
<link href="https://fonts.googleapis.com/css2?family=Poppins:wght@400;600&display=swap" rel="stylesheet">
<style>
  :root{
    --page:#e9e9e9;
    --paper:#ffffff;
    --navy:#2e4a5b;
    --navy-deep:#273f4e;
    --wine:#8c2347;
    --ink:#33495a;
    --flap:#f4f4f4;
    --flap-shade:#dcdcdc;
  }
  *{margin:0;padding:0;box-sizing:border-box}
  html,body{width:1200px;height:1200px;overflow:hidden;background:var(--page)}
  body{font-family:"Poppins",sans-serif;position:relative}
  .envelope{position:absolute;left:222px;width:756px;box-shadow:0 6px 18px rgba(0,0,0,.18)}
  .envelope-front{top:120px;height:420px;background:var(--paper)}
  .envelope-back{top:574px;height:504px;background:var(--navy)}
  .envelope svg.shape{position:absolute;inset:0;width:100%;height:100%}
  .brand{position:absolute;font-weight:600;letter-spacing:.5px;line-height:1}
  .envelope-front .brand{left:34px;top:44px;font-size:40px;color:var(--ink)}
  .envelope-back .brand{left:560px;top:432px;font-size:40px;color:var(--paper)}
  .contact-list{position:absolute;left:30px;top:302px;list-style:none;font-size:9.5px;color:var(--ink);line-height:1.25}
  .contact-list li{display:flex;align-items:center;gap:8px;margin-bottom:7px}
  .contact-list svg{width:15px;height:15px;flex:none}
</style>
</head>
<body>

<section class="envelope envelope-front">
  <svg class="shape" viewBox="0 0 756 420" preserveAspectRatio="none" aria-hidden="true">
    <path d="M566,0 C640,120 620,320 430,420 L756,420 L756,0 Z" fill="var(--navy)"/>
    <path d="M546,0 C622,122 602,318 416,420 L428,420 C614,322 634,120 562,0 Z" fill="var(--wine)"/>
  </svg>
  <div class="brand">Arcada</div>
  <ul class="contact-list">
    <li>
      <svg viewBox="0 0 16 16"><circle cx="8" cy="8" r="8" fill="var(--ink)"/><path d="M5.5 4.5l1.5 0 .6 1.8-1 .7a5 5 0 0 0 2.4 2.4l.7-1 1.8.6v1.5c0 .5-.4.9-.9.9A6.3 6.3 0 0 1 4.6 5.4c0-.5.4-.9.9-.9z" fill="#fff"/></svg>
      <span>11 4000-1234<br>11 4000-1234</span>
    </li>
    <li>
      <svg viewBox="0 0 16 16"><circle cx="8" cy="8" r="8" fill="var(--ink)"/><rect x="4" y="5" width="8" height="6" rx="1" fill="#fff"/><path d="M4.3 5.4L8 8.3l3.7-2.9" stroke="var(--ink)" stroke-width=".9" fill="none"/></svg>
      <span>contato@arcada.com</span>
    </li>
    <li>
      <svg viewBox="0 0 16 16"><circle cx="8" cy="8" r="8" fill="var(--ink)"/><path d="M5 11l6-6M9 5h2v2" stroke="#fff" stroke-width="1.4" fill="none" stroke-linecap="round"/></svg>
      <span>www.arcada.com</span>
    </li>
    <li>
      <svg viewBox="0 0 16 16"><circle cx="8" cy="8" r="8" fill="var(--ink)"/><path d="M8 3.5a3 3 0 0 0-3 3c0 2.2 3 5.8 3 5.8s3-3.6 3-5.8a3 3 0 0 0-3-3z" fill="#fff"/><circle cx="8" cy="6.5" r="1.1" fill="var(--ink)"/></svg>
      <span>Endereço Completo<br>Bairro - Cidade - Estado - Cep</span>
    </li>
  </ul>
</section>

<section class="envelope envelope-back">
  <svg class="shape" viewBox="0 0 756 504" preserveAspectRatio="none" aria-hidden="true">
    <defs>
      <linearGradient id="flap-fill" x1="0" y1="0" x2="0" y2="1">
        <stop offset="0" stop-color="var(--flap-shade)"/>
        <stop offset="1" stop-color="var(--flap)"/>
      </linearGradient>
    </defs>
    <rect x="0" y="0" width="756" height="70" fill="var(--flap-shade)"/>
    <path d="M18,0 H738 L706,108 Q698,134 668,134 H88 Q58,134 50,108 Z" fill="url(#flap-fill)"/>
  </svg>
  <div class="brand">Arcada</div>
</section>

</body>
</html>
```